Business Cards for new orthopaedic surgery practice

My husband and I are starting our own orthopaedic surgery practice. We are looking for a business card that is uniform, but one will have my name/title and the other will have his. You can just create one design with my name on it for now. But when I choose your design as the winning design I will ask that you add another copy with his name/title.

We are looking for classy, simple, elite all in one. We like dark blues/a little gold/yellow. Something that goes with our logo. We want our logo incorporated. Here is all the info you need:
Business name: RV Spine & Vitality Center
Location: 38915 North Bramble Ave
Coral Springs, FL 33071
Phone: 954-218-4630
Fax: 954-571-2846
Email: info@myrvspine.example

Names: Lucinda Ferrow, M.D.
Board Certified Hand and Upper Extremity Surgeon

Emeka Dlunga, M.D.
Board Certified Hip & Knee Replacement/General Orthopaedic Surgeon

Can decide what you want to put on the back. Maybe a slogan:
Rooted in Care. Focused on You

I am just going to upload our logo. The only thing is if we select you as the winning design, the location, and phone numbers may change. We will need your help to update that once fully solidified.

Industry/Entity Type

Medical

Contact Information for Business Card

Colors
0054AA
0677BA
7BADD7
CADEEF
E8F1F8
0094D4
00A9DD
6FCCEA
C7EBF8
E9F6FB

Requirements
Must have
• class, appeal,
Should not have
• We want to air on the side of masculine if we are looking at masculine vs. feminine feel. But we still want it classy, sophisticated, and something we will love

```html
<!DOCTYPE html>
<html lang="en">
<head>
<meta charset="utf-8">
<title>RV Spine &amp; Vitality Center — Business Card</title>
<link rel="stylesheet" href="https://fonts.googleapis.com/css2?family=Poppins:wght@400;600;700&display=swap">
<style>
  :root {
    --stage: #7b7d80;
    --paper: #f7f8f9;
    --navy: #1f3f97;
    --deep: #1a2f86;
    --cyan: #1fa9de;
    --ink: #1d1d22;
    --back-start: #1b2f86;
    --back-mid: #0d5fb3;
    --back-end: #27a8e0;
  }
  * { box-sizing: border-box; margin: 0; padding: 0; }
  html, body { width: 1200px; height: 824px; overflow: hidden; }
  body {
    background: var(--stage);
    font-family: "Poppins", sans-serif;
    position: relative;
  }
  .card {
    position: absolute;
    width: 560px;
    height: 320px;
    border-radius: 3px;
    box-shadow: 0 18px 40px rgba(0,0,0,0.28);
    overflow: hidden;
  }
  .card--front { left: 70px; top: 90px; background: var(--paper); }
  .card--back {
    left: 570px; top: 414px;
    background: linear-gradient(115deg, var(--back-start) 0%, var(--back-mid) 55%, var(--back-end) 100%);
  }

  .brand {
    display: flex; align-items: center; gap: 10px;
    font-weight: 600; letter-spacing: 0.04em; text-transform: uppercase;
  }
  .brand__dot { width: 14px; height: 14px; border-radius: 50%; flex: none; }
  .brand__name { font-size: 13px; line-height: 1.25; }

  .card--front .brand { position: absolute; left: 40px; top: 40px; color: var(--navy); }
  .card--front .brand__dot { background: var(--navy); }

  .divider {
    position: absolute; left: 34px; right: 0; top: 186px;
    height: 1.5px; background: var(--navy);
  }
  .holder__name {
    position: absolute; left: 40px; top: 146px;
    font-size: 28px; font-weight: 700; color: var(--navy); line-height: 1.2;
  }
  .holder__title {
    position: absolute; left: 40px; top: 193px;
    font-size: 10.5px; font-weight: 400; color: var(--cyan);
  }

  .contacts {
    position: absolute; left: 40px; top: 232px; right: 20px;
    display: grid; grid-template-columns: 128px 1fr; row-gap: 12px; column-gap: 16px;
    font-size: 12px; color: var(--ink);
  }
  .contact { display: flex; align-items: center; gap: 10px; white-space: nowrap; }
  .contact__icon { width: 18px; height: 18px; flex: none; }

  .card--back .brand {
    position: absolute; left: 50%; top: 50%; transform: translate(-50%, -50%);
    color: #ffffff; gap: 12px; white-space: nowrap;
  }
  .card--back .brand__dot { background: #ffffff; width: 16px; height: 16px; }
  .card--back .brand__name { font-size: 16px; }
</style>
</head>
<body>

  <section class="card card--front" aria-label="Business card front">
    <div class="brand">
      <span class="brand__dot"></span>
      <span class="brand__name">RV Spine &amp; Vitality Center</span>
    </div>

    <h1 class="holder__name">Emeka Dlunga, M.D.</h1>
    <div class="divider"></div>
    <p class="holder__title">Board Certified Hip &amp; Knee Replacement/General Orthopaedic Surgeon</p>

    <div class="contacts">
      <div class="contact">
        <svg class="contact__icon" viewBox="0 0 18 18" aria-hidden="true">
          <circle cx="9" cy="9" r="9" fill="#1fa9de"/>
          <path d="M6.2 4.8c.4-.3.9-.2 1.1.2l.8 1.4c.2.4.1.8-.2 1l-.6.5c.4 1 1.2 1.8 2.2 2.2l.5-.6c.3-.3.7-.4 1-.2l1.4.8c.4.2.5.7.2 1.1l-.6.8c-.4.5-1 .6-1.6.4-2.3-.8-4-2.5-4.8-4.8-.2-.6 0-1.2.4-1.6z" fill="#fff"/>
        </svg>
        <span>954-218-4630</span>
      </div>
      <div class="contact">
        <svg class="contact__icon" viewBox="0 0 18 18" aria-hidden="true">
          <circle cx="9" cy="9" r="9" fill="#1fa9de"/>
          <path d="M9 3.8c-2 0-3.5 1.5-3.5 3.4 0 2.5 3.5 6.4 3.5 6.4s3.5-3.9 3.5-6.4c0-1.9-1.5-3.4-3.5-3.4z" fill="#fff"/>
          <circle cx="9" cy="7.3" r="1.3" fill="#1fa9de"/>
        </svg>
        <span>38915 North Bramble Ave, Coral Springs, FL 33071</span>
      </div>
      <div class="contact">
        <svg class="contact__icon" viewBox="0 0 18 18" aria-hidden="true">
          <circle cx="9" cy="9" r="9" fill="#1fa9de"/>
          <rect x="6" y="4.5" width="6" height="3" fill="#fff"/>
          <rect x="4.3" y="7.3" width="9.4" height="4.6" rx="1" fill="#fff"/>
          <rect x="6" y="10.3" width="6" height="3.2" fill="#fff" stroke="#1fa9de" stroke-width="0.8"/>
        </svg>
        <span>954-571-2846</span>
      </div>
      <div class="contact">
        <svg class="contact__icon" viewBox="0 0 18 18" aria-hidden="true">
          <circle cx="9" cy="9" r="9" fill="#1fa9de"/>
          <rect x="4.5" y="5.8" width="9" height="6.4" rx="0.8" fill="#fff"/>
          <path d="M4.8 6.2 9 9.4l4.2-3.2" fill="none" stroke="#1fa9de" stroke-width="0.9"/>
        </svg>
        <span>info@myrvspine.example</span>
      </div>
    </div>
  </section>

  <section class="card card--back" role="img" aria-label="Card back: deep blue to bright cyan gradient behind the practice name">
    <div class="brand">
      <span class="brand__dot"></span>
      <span class="brand__name">RV Spine &amp; Vitality Center</span>
    </div>
  </section>

</body>
</html>
```